I need a website for my moving company Bolt Hauling LLC. I would like the following text included in my website. I have purchased the domain bolthaulingcrew.example from siteburrow.example. I am not familiar with SEO or other techniques that help my page on search engines but would like the website to be optimized for Findora search engine. I have attached our logo below and would like it to be used in the design. The colors in the logo can be used also in the design.
Home/About Us
At Bolt Hauling LLC, we know moving. It can be difficult, stressful, and a real pain in the backside. But it doesn’t have to be! When you partner with Bolt, you get the benefits of a professional moving team that is licensed and insured for your protection along with years of experience and a dedication to providing the highest quality service, each and every time.
Our Services
We do a wide variety of local moves, including apartments, single-family homes, retirement communities, dorms, condos, and many more! Our movers are trained to protect your belongings and your home – all pieces of furniture are padded and stretch wrapped free of charge, ensuring your items and home are damage-free at the end of your move. Having added stress about packing up your home prior to moving? We’ve got you covered with our full service packing and unpacking services, too.
What You Get
When you partner with BOLT, you’ll get the best service in the industry, as well as:
* The Use of Packing & Moving Materials: The hourly rate includes the use of our dollies, ratchet straps, pads, moving tools, and property protection like floor mats, door-jamb protectors, stairwell protectors, and plenty of muscle!
• Trained, Licensed, and Insured Movers: All of our movers are highly trained to provide you with the best service, and to ensure the protection of you and your items.
• Professional: Honest, Uniformed, Nice, Knowledgeable Service is what you’ll get with every member of our moving teams.
• Custom Service for Every Move: Every move is as unique as the person or business moving. Our training and equipment allows us to customize every project to ensure the very best for every client.
Target Market(s)
Home and Business movers
Industry/Entity Type
Moving Company
Colors
Designer to choose colors to be used in the design.
Requirements
Must have
- 2 sides
Nice to have
- Colorful design with logo included.
Should not have
- animated characters

```html
<!DOCTYPE html>
<html lang="en">
<head>
<meta charset="utf-8">
<title>Bolt Hauling LLC – Fast Moving</title>
<link rel="stylesheet" href="https://fonts.googleapis.com/css2?family=Roboto:wght@300;400;500;700&display=swap">
<style>
:root{
  --green:#8cc63f;
  --green-dark:#76ad2e;
  --orange:#f7941d;
  --ink:#2b2b2b;
  --muted:#666;
  --soft:#f6f6f6;
  --dark:#4a4a4a;
  --footer:#333;
  --white:#fff;
}
*{box-sizing:border-box;margin:0;padding:0}
html,body{width:1200px;height:4225px;overflow:hidden}
body{font-family:"Roboto",sans-serif;color:var(--ink);background:var(--white);position:relative}
.abs{position:absolute}
.photo{position:absolute}
.btn{position:absolute;display:flex;align-items:center;justify-content:center;font-size:14px;font-weight:500;letter-spacing:.5px;text-transform:uppercase}
.btn-green{background:var(--green);color:var(--white)}
.btn-orange{background:var(--orange);color:var(--white)}
.btn-outline{border:2px solid var(--green);color:var(--green)}
.brand{display:flex;align-items:center;gap:10px;font-weight:700;font-size:22px;color:var(--green);letter-spacing:.5px}
.brand-mark{width:22px;height:22px;background:var(--orange)}
.eyebrow{font-size:18px;color:var(--green)}
.heading{font-size:38px;font-weight:400;color:var(--ink)}
.body-text{font-size:16px;line-height:1.7;color:var(--muted)}

/* hero */
.hero{position:absolute;left:0;top:0;width:1200px;height:676px}
.hero-photo{inset:0;background:linear-gradient(120deg,#9a9c9b 0%,#c9b9a2 45%,#b9a488 70%,#8e8e8e 100%)}
.hero-shade{position:absolute;inset:0;background:rgba(0,0,0,.18)}
.nav{position:absolute;left:0;top:0;width:1200px;height:70px}
.nav .brand{position:absolute;left:55px;top:22px;color:var(--orange)}
.nav-link{position:absolute;top:26px;font-size:14px;font-weight:500;color:var(--white)}
.hero-title{position:absolute;left:0;width:1200px;top:280px;text-align:center;font-size:96px;font-weight:300;color:var(--white)}
.hero-cta{position:absolute;left:608px;top:393px;display:flex;align-items:center;gap:18px;font-size:26px;color:var(--white);font-weight:300}
.play{width:62px;height:62px;border-radius:50%;background:var(--orange);display:flex;align-items:center;justify-content:center}
.hero-call{position:absolute;right:60px;top:620px;font-size:28px;color:var(--white)}
.hero-call span{color:var(--green)}

/* how it works */
.how{position:absolute;left:0;top:676px;width:1200px;height:479px}
.how .eyebrow{position:absolute;top:62px;width:1200px;text-align:center}
.how .heading{position:absolute;top:88px;width:1200px;text-align:center;font-size:44px}
.step{position:absolute;top:190px;width:300px;text-align:center}
.step svg{display:block;margin:0 auto}
.step h3{margin-top:32px;font-size:28px;font-weight:400}
.step p{margin-top:14px;font-size:14px;line-height:1.55;color:var(--muted)}
.step-line{position:absolute;top:248px;height:2px;background:#e2e2e2}

/* experienced */
.exp{position:absolute;left:0;top:1155px;width:1200px;height:535px;background:var(--soft)}
.exp-block{position:absolute;left:0;top:260px;width:195px;height:250px;background:var(--green)}
.exp-photo{left:45px;top:55px;width:540px;height:395px;background:linear-gradient(135deg,#eceae6 0%,#c9a57a 45%,#3f6fae 60%,#d8c2a0 100%);box-shadow:0 4px 14px rgba(0,0,0,.15)}
.exp-text{position:absolute;left:655px;top:80px;width:500px}
.exp-text .tag{font-size:16px;color:var(--orange)}
.exp-text .heading{margin-top:10px;font-size:36px}
.exp-text .body-text{margin-top:22px;font-size:15px}

/* guarantee */
.guar{position:absolute;left:0;top:1690px;width:1200px;height:457px}
.guar-text{position:absolute;left:75px;top:75px;width:470px}
.guar-text .heading{margin-top:8px;font-size:36px}
.guar-text .body-text{margin-top:16px;font-size:15px}
.checklist{list-style:none;margin-top:24px}
.checklist li{position:relative;padding-left:22px;font-size:16px;color:var(--ink);line-height:2.2}
.checklist li::before{content:"";position:absolute;left:2px;top:14px;width:8px;height:8px;border-radius:50%;background:var(--green)}
.guar-accent{position:absolute;left:1140px;top:205px;width:60px;height:210px;background:var(--orange)}
.guar-photo{left:600px;top:15px;width:540px;height:400px;background:linear-gradient(130deg,#e8e2d6 0%,#c8a77d 40%,#a4c05a 70%,#efe9dd 100%)}

/* services */
.services{position:absolute;left:0;top:2147px;width:1200px;height:507px;background:var(--dark)}
.services h2{position:absolute;top:100px;width:1200px;text-align:center;font-size:34px;font-weight:400;color:var(--orange)}
.services p{position:absolute;left:140px;top:160px;width:920px;text-align:center;font-size:16px;line-height:1.75;color:#eee}

/* booking */
.booking{position:absolute;left:0;top:2654px;width:1200px;height:402px}
.booking-photo{inset:0;background:linear-gradient(90deg,#8cc63f 0%,#9ccd55 50%,#86bf3a 100%)}
.booking-text{position:absolute;left:95px;top:120px;width:420px;text-align:center;color:var(--white)}
.booking-text h2{font-size:34px;font-weight:400}
.booking-text p{margin-top:14px;font-size:13px;line-height:1.6}
.price-card{position:absolute;left:625px;top:-19px;width:440px;height:430px;background:var(--white);box-shadow:0 6px 20px rgba(0,0,0,.18);text-align:center}
.price-card h3{margin-top:70px;font-size:32px;font-weight:400}
.price-card .dur{margin-top:14px;font-size:20px;color:#888}
.price-card .price{margin-top:14px;font-size:48px;font-weight:500}

/* subscribe */
.subscribe{position:absolute;left:0;top:3056px;width:1200px;height:606px}
.subscribe h2{position:absolute;top:98px;width:1200px;text-align:center;font-size:34px;font-weight:400}
.subscribe .lead{position:absolute;top:150px;width:1200px;text-align:center;font-size:16px;color:var(--muted)}
.email-field{position:absolute;left:327px;top:212px;width:506px;height:50px;border:2px solid #777;padding:0 16px;display:flex;align-items:center;font-size:14px;color:#888}
.sub-photo{left:0;top:340px;width:1200px;height:266px;background:linear-gradient(180deg,#ffffff 0%,#f1ece4 35%,#d8c3a4 75%,#b89670 100%)}

/* footer */
.contact{position:absolute;left:0;top:3662px;width:1200px;height:465px}
.contact .brand{position:absolute;left:38px;top:48px;color:var(--orange)}
.contact h3{position:absolute;left:35px;top:128px;font-size:24px;font-weight:400}
.contact .intro{position:absolute;left:35px;top:172px;width:360px;font-size:15px;line-height:1.5;color:var(--muted)}
.contact .co{position:absolute;left:35px;top:236px;font-size:16px}
.contact .addr{position:absolute;left:35px;top:286px;font-size:16px}
.contact .phone{position:absolute;left:35px;top:322px;font-size:28px}
.map{left:455px;top:50px;width:693px;height:363px;background:linear-gradient(135deg,#e9e9e6 0%,#dfe3dc 60%,#e8e6e1 100%)}
.bottom-bar{position:absolute;left:0;top:4127px;width:1200px;height:98px;background:var(--footer)}
.bottom-bar p{position:absolute;left:35px;top:40px;font-size:12px;color:#bbb}
.social{position:absolute;top:36px;width:28px;height:28px;border-radius:50%}
</style>
</head>
<body>

<header class="hero">
  <div class="photo hero-photo" role="img" aria-label="Smiling couple unpacking moving boxes in their new home"></div>
  <div class="hero-shade"></div>
  <nav class="nav">
    <div class="brand"><span class="brand-mark"></span>BOLT HAULING</div>
    <span class="nav-link" style="left:675px">HOW IT WORKS</span>
    <span class="nav-link" style="left:810px">PRICING</span>
    <span class="nav-link" style="left:907px">CONTACT</span>
    <span class="btn btn-green" style="left:1020px;top:15px;width:115px;height:40px">Book Now</span>
  </nav>
  <h1 class="hero-title">Fast Moving ?</h1>
  <div class="hero-cta">See How We Do It
    <span class="play"><svg width="20" height="22" viewBox="0 0 20 22"><path d="M3 2 L18 11 L3 20 Z" fill="#fff"/></svg></span>
  </div>
  <div class="hero-call"><span>Call :</span> (555) 014-2290</div>
</header>

<section class="how">
  <div class="eyebrow">The easy way to move</div>
  <h2 class="heading">How it works</h2>
  <div class="step-line" style="left:420px;width:120px"></div>
  <div class="step-line" style="left:700px;width:130px"></div>
  <div class="step" style="left:195px">
    <svg width="90" height="90" viewBox="0 0 90 90" fill="none" stroke="#333" stroke-width="2.5">
      <rect x="12" y="8" width="66" height="74" rx="3"/><line x1="12" y1="20" x2="78" y2="20"/>
      <path d="M28 50 L45 36 L62 50" stroke="#8cc63f"/><rect x="33" y="50" width="24" height="20" stroke="#8cc63f"/>
    </svg>
    <h3>Order</h3>
    <p>Lorem Ipsum is simply dummy text of<br>the printing and typesetting industry.<br>Lorem Ipsum has been the industry's</p>
  </div>
  <div class="step" style="left:470px">
    <svg width="100" height="90" viewBox="0 0 100 90" fill="none" stroke="#333" stroke-width="2.5">
      <rect x="6" y="24" width="52" height="40"/><path d="M58 36 H78 L92 50 V64 H58"/>
      <circle cx="24" cy="70" r="7"/><circle cx="76" cy="70" r="7"/>
      <rect x="20" y="32" width="22" height="22" stroke="#8cc63f"/><path d="M31 50 V38 M26 43 L31 38 L36 43" stroke="#8cc63f"/>
    </svg>
    <h3>Move</h3>
    <p>Lorem Ipsum is simply dummy text of<br>the printing and typesetting industry.<br>Lorem Ipsum has been the industry's</p>
  </div>
  <div class="step" style="left:755px">
    <svg width="90" height="90" viewBox="0 0 90 90" fill="none" stroke="#333" stroke-width="2.5">
      <path d="M10 40 L45 10 L80 40"/><rect x="18" y="38" width="54" height="42"/>
      <rect x="38" y="56" width="14" height="24" stroke="#8cc63f"/><rect x="24" y="46" width="10" height="10"/><rect x="56" y="46" width="10" height="10"/>
    </svg>
    <h3>Unpack</h3>
    <p>Lorem Ipsum is simply dummy text of<br>the printing and typesetting industry.<br>Lorem Ipsum has been the industry's</p>
  </div>
</section>

<section class="exp">
  <div class="exp-block"></div>
  <div class="photo exp-photo" role="img" aria-label="Two uniformed movers carrying a white sofa past stacked boxes"></div>
  <div class="exp-text">
    <div class="tag">boltmoving</div>
    <h2 class="heading">Experienced &amp; Reliable</h2>
    <p class="body-text">At Bolt Hauling LLC, we know moving. It can be difficult, stressful, and a real pain in the backside. But it doesn't have to be! When you partner with Bolt, you get the benefits of a professional moving team that is licensed and insured for your protection along with years of experience and a dedication to providing the highest quality service, each and every time.</p>
  </div>
  <span class="btn btn-outline" style="left:655px;top:320px;width:150px;height:55px">Read More</span>
</section>

<section class="guar">
  <div class="guar-text">
    <div class="eyebrow" style="font-size:16px">Fully insured</div>
    <h2 class="heading">Our Gaurantee</h2>
    <p class="body-text">When you partner with BOLT, you'll get the best service in the industry, as well as:</p>
    <ul class="checklist">
      <li>The unlimited use of packing &amp; moving materials</li>
      <li>Trained, Licensed, and Insured Movers</li>
      <li>A Professional service catering to your specific needs</li>
    </ul>
  </div>
  <div class="guar-accent"></div>
  <div class="photo guar-photo" role="img" aria-label="Couple packing belongings into a cardboard box"></div>
</section>

<section class="services">
  <h2>Our Services</h2>
  <p>Bolt Hauling LLC in Cedarvale does a wide variety of local moves, including apartments, single-family homes, retirement communities, dorms, condos, and many more! Our movers are trained to protect your belongings and your home – all pieces of furniture are padded and stretch wrapped free of charge, ensuring your items and home are damage-free at the end of your move. Having added stress about packing up your home prior to moving? We've got you covered with our full service packing and unpacking services, too.</p>
  <span class="btn btn-outline" style="left:525px;top:338px;width:150px;height:55px">Read More</span>
</section>

<section class="booking">
  <div class="photo booking-photo" role="img" aria-label="Green tinted photo of movers at work"></div>
  <div class="booking-text">
    <h2>Book an Apportment</h2>
    <p>Lorem Ipsum is simply dummy text of the printing and<br>typesetting industry. Lorem Ipsum has been the industry's</p>
  </div>
  <div class="price-card">
    <h3>Moving Service</h3>
    <div class="dur">1 hour</div>
    <div class="price">$125.00</div>
    <span class="btn btn-orange" style="left:127px;top:285px;width:188px;height:55px">Book Now</span>
  </div>
</section>

<section class="subscribe">
  <h2>Subscribe</h2>
  <p class="lead">Sign up to hear from us about specials, packing tips, and more.</p>
  <div class="email-field">Enter your email address</div>
  <span class="btn btn-green" style="left:512px;top:284px;width:138px;height:44px;font-size:13px">Subscribe Now</span>
  <div class="photo sub-photo" role="img" aria-label="Couple sitting on the floor among moving boxes"></div>
</section>

<footer class="contact">
  <div class="brand"><span class="brand-mark"></span>BOLT HAULING</div>
  <h3>Schedule Your Move</h3>
  <p class="intro">To arrange movers, please contact us at your convenience.&nbsp; We look forward to meeting you soon.</p>
  <div class="co">Bolt Hauling LLC</div>
  <div class="addr">412 Larkspur Ave., Cedarvale, MS 39000, US</div>
  <div class="phone">(555) 014-2290</div>
  <span class="btn btn-green" style="left:30px;top:378px;width:140px;height:45px;font-size:13px">Message Now</span>
  <div class="photo map" role="img" aria-label="Street map showing the office location"></div>
</footer>

<div class="bottom-bar">
  <p>Copyright © 2017 Bolt Hauling LLC - All Rights Reserved</p>
  <span class="social" style="left:991px;background:#3b5998"></span>
  <span class="social" style="left:1031px;background:#1da1f2"></span>
  <span class="social" style="left:1075px;background:#0077b5"></span>
  <span class="social" style="left:1121px;background:#6fbf4a"></span>
</div>

</body>
</html>
```